New Business Card

We need to refresh our business cards. We designed these ourselves and we have no graphic design experience. We would like to find a new business card design that is professional and unique. We are an auto finance company. Feel free to play with the logo, but we would like to keep the eye very present on the card. Our corporate colors are green, grey, and white.
Green - RGB - 168,215,27; HEX - #AADD22
Grey - RGB - 196,196,196; HEX - #C4C4C4
Updates
Need to upload the vector file to finalize the project. The last logo was for a jpeg that didn't stretch well.
Industry/Entity Type
Financial Service
Contact Information for Business Card
Honestly don't know...I need your help!

```html
<!DOCTYPE html>
<html lang="en">
<head>
<meta charset="utf-8">
<title>Clearway Capital – Business Card</title>
<link rel="stylesheet" href="https://fonts.googleapis.com/css2?family=Source+Sans+3:wght@600;700&display=swap">
<style>
  :root {
    --green: #aadd22;
    --lime: #a8ff00;
    --grey: #c4c4c4;
    --band: #e6e8e7;
    --white: #ffffff;
    --stage: #768280;
  }
  * { margin: 0; padding: 0; box-sizing: border-box; }
  html, body {
    width: 1200px; height: 1200px; overflow: hidden;
    background: var(--stage);
    font-family: "Source Sans 3", "Segoe UI", Arial, sans-serif;
  }
  .card {
    position: absolute; left: 225px;
    width: 750px; height: 428px;
    background: var(--white); overflow: hidden;
  }
  .card--front { top: 99px; }
  .card--back { top: 632px; }
  .card__shapes { position: absolute; inset: 0; }
  .brand {
    position: absolute; width: 316px; text-align: center;
    color: var(--lime); font-weight: 600; font-size: 36px; line-height: 1;
  }
  .card--front .brand { left: 74px; top: 228px; }
  .card--back .brand { left: 360px; top: 231px; }
  .tagline {
    position: absolute; right: 68px; top: 139px;
    color: var(--lime); font-weight: 700; font-size: 46px;
    font-variant: small-caps; line-height: 41px; text-align: right;
    letter-spacing: 0.5px;
  }
  .contact-list { list-style: none; }
  .contact-item {
    position: absolute; left: 111px;
    color: var(--lime); font-weight: 700; font-size: 21px; line-height: 1;
    transform: translateY(-50%);
  }
  .support {
    position: absolute; left: 20px; top: 367px;
    color: var(--lime); font-weight: 700; font-size: 22px;
  }
  .support__label { font-variant: small-caps; font-size: 17px; letter-spacing: 0.5px; }
</style>
</head>
<body>

<section class="card card--front" aria-label="Business card front">
  <svg class="card__shapes" width="750" height="428" viewBox="0 0 750 428" aria-hidden="true">
    <rect x="0" y="0" width="189" height="428" fill="var(--lime)"/>
    <circle cx="232" cy="213" r="218" fill="var(--white)"/>
    <circle cx="232" cy="213" r="188" fill="var(--lime)"/>
    <circle cx="232" cy="213" r="158" fill="var(--white)"/>
    <circle cx="232" cy="165" r="34" fill="var(--grey)"/>
    <line x1="688" y1="129" x2="688" y2="295" stroke="var(--grey)" stroke-width="2"/>
  </svg>
  <p class="brand">Clearway Capital</p>
  <p class="tagline">Auto<br>Finance<br>Company</p>
</section>

<section class="card card--back" aria-label="Business card back">
  <svg class="card__shapes" width="750" height="428" viewBox="0 0 750 428" aria-hidden="true">
    <rect x="0" y="358" width="393" height="45" fill="var(--band)"/>
    <rect x="570" y="0" width="180" height="428" fill="var(--lime)"/>
    <circle cx="518" cy="216" r="218" fill="var(--white)"/>
    <circle cx="518" cy="216" r="188" fill="var(--lime)"/>
    <circle cx="518" cy="216" r="158" fill="var(--white)"/>
    <circle cx="518" cy="168" r="34" fill="var(--grey)"/>

    <g class="contact-tab">
      <rect x="0" y="84" width="72" height="42" fill="var(--lime)"/>
      <circle cx="66" cy="105" r="24" fill="var(--lime)"/>
      <circle cx="66" cy="105" r="18" fill="none" stroke="var(--white)" stroke-width="2"/>
      <rect x="60" y="95" width="12" height="20" rx="2" fill="none" stroke="var(--white)" stroke-width="2"/>
    </g>
    <g class="contact-tab">
      <rect x="0" y="150" width="72" height="42" fill="var(--lime)"/>
      <circle cx="66" cy="171" r="24" fill="var(--lime)"/>
      <circle cx="66" cy="171" r="18" fill="none" stroke="var(--white)" stroke-width="2"/>
      <rect x="56" y="164" width="12" height="9" rx="1" fill="var(--white)"/>
      <rect x="64" y="167" width="13" height="9" rx="1" fill="var(--white)" stroke="var(--lime)" stroke-width="1.5"/>
    </g>
    <g class="contact-tab">
      <rect x="0" y="213" width="72" height="42" fill="var(--lime)"/>
      <circle cx="66" cy="234" r="24" fill="var(--lime)"/>
      <circle cx="66" cy="234" r="18" fill="none" stroke="var(--white)" stroke-width="2"/>
      <rect x="57" y="228" width="18" height="12" fill="none" stroke="var(--white)" stroke-width="2"/>
      <polyline points="57,228 66,235 75,228" fill="none" stroke="var(--white)" stroke-width="2"/>
    </g>
    <g class="contact-tab">
      <rect x="0" y="277" width="72" height="42" fill="var(--lime)"/>
      <circle cx="66" cy="298" r="24" fill="var(--lime)"/>
      <circle cx="66" cy="298" r="18" fill="none" stroke="var(--white)" stroke-width="2"/>
      <circle cx="66" cy="298" r="10" fill="none" stroke="var(--white)" stroke-width="1.6"/>
      <ellipse cx="66" cy="298" rx="4.5" ry="10" fill="none" stroke="var(--white)" stroke-width="1.6"/>
      <line x1="56" y1="298" x2="76" y2="298" stroke="var(--white)" stroke-width="1.6"/>
    </g>
  </svg>

  <ul class="contact-list">
    <li class="contact-item" style="top:105px">888-555-0142</li>
    <li class="contact-item" style="top:171px">Online Chat</li>
    <li class="contact-item" style="top:234px">help@clearway.com</li>
    <li class="contact-item" style="top:298px">www.clearway.com</li>
  </ul>
  <p class="brand">Clearway Capital</p>
  <p class="support"><span class="support__label">Technical Support</span> :- 801-555-0197</p>
</section>

</body>
</html>
```